Restoration Specialist in need of business card designs

One side of the business card is a bathroom ripped out down to the studs with just a sink and toilet and then the other side is the bathroom (same sink and toilet) but put back together. Like a before and after on each side behind our information. Stand out, hard to forget, business cards for my restoration company. I want a unique concept all together.
Must include in no particular order:
our business name "Summit Renewals"
Possible Logo for a restoration company
Owner; Dennis Moravec
410-386-7294
dmoravec@summitrenewalsqx.example
SummitRenewalsQX.example (our company website) BUT I am open to any and all designs and options.

Target Market(s)

Customers, Men in the mitigation, plumbing, electrical, HVAC, Roofing, insurance companies

Industry/Entity Type

Restoration/ construction

Contact Information for Business Card

Must include in no particular order: our business name "Summit Renewals" Owner; Dennis Moravec 410-386-7294 dmoravec@summitrenewalsqx.example SummitRenewalsQX.example (our company website) MAY include a list of our services: Residential~ Emergency Response ~ Board- up~ Complete Restoration

Font styles to use
Serif

Colors
0054AA
0677BA
7BADD7
CADEEF
E8F1F8
F0912C
F2A743
F7CA91
FBE8D2
FDF5EE

Requirements
Must have
• unique, memorable, not something men have seen over and over again,
Nice to have
• eye catching
Should not have
• Been something I could have made by myself

```html
<!DOCTYPE html>
<html lang="en">
<head>
<meta charset="utf-8">
<title>Summit Renewals – Business Card</title>
<link rel="stylesheet" href="https://fonts.googleapis.com/css2?family=Crimson+Pro:wght@700&family=Arimo:wght@400&family=Roboto+Condensed:wght@400&display=swap">
<style>
  :root {
    --backdrop: #3f3f3f;
    --card: #12364f;
    --orange: #ef7a22;
    --white: #ffffff;
    --emboss-blue: #2b8cc4;
    --rule: rgba(255,255,255,0.35);
  }
  * { margin: 0; padding: 0; box-sizing: border-box; }
  html, body {
    width: 1200px; height: 1200px; overflow: hidden;
    background: var(--backdrop);
  }
  .canvas { position: relative; width: 1200px; height: 1200px; }
  .card {
    position: absolute; left: 256px; width: 688px; height: 393px;
    background: var(--card); border-radius: 26px; overflow: hidden;
  }
  .card--front { top: 159px; }
  .card--back { top: 653px; }

  /* Front */
  .brand-block {
    position: absolute; left: 96px; top: 110px; width: 180px;
    display: flex; flex-direction: column; align-items: center;
  }
  .brand-mark {
    width: 16px; height: 16px; background: var(--orange); margin-bottom: 14px;
  }
  .brand-name {
    font-family: "Crimson Pro", serif; font-weight: 700;
    color: var(--orange); text-align: center;
    font-size: 34px; line-height: 1.02; letter-spacing: 0.5px;
  }
  .divider {
    position: absolute; left: 302px; top: 96px; width: 1px; height: 192px;
    background: linear-gradient(to bottom, transparent, var(--rule) 20%, var(--rule) 80%, transparent);
  }
  .person { position: absolute; left: 328px; top: 108px; }
  .person__name {
    font-family: "Crimson Pro", serif; font-weight: 700;
    color: var(--white); font-size: 24px; letter-spacing: 0.6px; line-height: 1;
  }
  .person__role {
    font-family: "Arimo", sans-serif; color: var(--orange);
    font-size: 15px; margin-top: 5px;
  }
  .contacts {
    position: absolute; left: 328px; top: 213px; list-style: none;
  }
  .contacts__item {
    display: flex; align-items: center; height: 20.5px;
    font-family: "Arimo", sans-serif; font-size: 16px; color: var(--white);
  }
  .contacts__icon { width: 14px; height: 14px; margin-right: 11px; flex: none; }

  /* Back */
  .brand-hero {
    position: absolute; left: 0; right: 0; top: 108px;
    display: flex; flex-direction: column; align-items: center;
  }
  .brand-hero__name {
    font-family: "Crimson Pro", serif; font-weight: 700;
    color: var(--emboss-blue); text-align: center;
    font-size: 68px; line-height: 1; letter-spacing: 1px;
  }
  .services {
    position: absolute; left: 0; right: 0; top: 337px;
    display: flex; justify-content: center; align-items: center;
    font-family: "Roboto Condensed", sans-serif; font-size: 17px; color: var(--white);
    list-style: none;
  }
  .services__item + .services__item::before {
    content: ""; display: inline-block; width: 6px; height: 6px;
    background: var(--orange); margin: 0 7px 3px; vertical-align: middle;
  }
</style>
</head>
<body>
<main class="canvas">
  <section class="card card--front" aria-label="Business card front">
    <div class="brand-block">
      <span class="brand-mark"></span>
      <div class="brand-name">SUMMIT<br>RENEWALS</div>
    </div>
    <div class="divider"></div>
    <div class="person">
      <div class="person__name">DENNIS MORAVEC</div>
      <div class="person__role">Owner</div>
    </div>
    <ul class="contacts">
      <li class="contacts__item">
        <svg class="contacts__icon" viewBox="0 0 24 24"><path fill="#ef7a22" d="M6.6 10.8a15.1 15.1 0 0 0 6.6 6.6l2.2-2.2c.3-.3.7-.4 1-.2 1.1.4 2.3.6 3.6.6.6 0 1 .4 1 1V20c0 .6-.4 1-1 1A17 17 0 0 1 3 4c0-.6.4-1 1-1h3.5c.6 0 1 .4 1 1 0 1.3.2 2.5.6 3.6.1.3 0 .7-.2 1z"/></svg>
        410-386-7294
      </li>
      <li class="contacts__item">
        <svg class="contacts__icon" viewBox="0 0 24 24"><rect x="2" y="5" width="20" height="14" fill="#ef7a22"/><path d="M2 5l10 8 10-8" fill="none" stroke="#12364f" stroke-width="2"/></svg>
        dmoravec@summitrenewalsqx.example
      </li>
      <li class="contacts__item">
        <svg class="contacts__icon" viewBox="0 0 24 24"><circle cx="12" cy="12" r="10" fill="#ef7a22"/><path d="M7 6c2 1 3 3 2 5s1 3 0 5M15 4c-1 2 1 3 3 4M14 14c2 0 3 2 2 5" fill="none" stroke="#12364f" stroke-width="1.6"/></svg>
        www.SummitRenewalsQX.example
      </li>
    </ul>
  </section>

  <section class="card card--back" aria-label="Business card back">
    <div class="brand-hero">
      <div class="brand-hero__name">SUMMIT<br>RENEWALS</div>
    </div>
    <ul class="services">
      <li class="services__item">Residential</li>
      <li class="services__item">Emergency Response</li>
      <li class="services__item">Board- up</li>
      <li class="services__item">Storm Protection</li>
      <li class="services__item">Complete Restoration</li>
    </ul>
  </section>
</main>
</body>
</html>
```